Indoor Gun Range Web Design Project

Create a professional bold indoor gun range website. Logo colors are white, red, and black. This is a very professional gun range. Please use high quality stock images if possible. Stay away from a lot of militia type photos. Use your best judgement on what to put as a main image and headline.

Here are some websites that I like for design.

http://www.pinebrookarsenal.example/
http://www.layoutbazaar.example/website-templates/51947.html
http://www.marigoldworks.example/

Target Market(s)

Men ages 25-65

Industry/Entity Type

Gun

Requirements
Must have
• Bold lettering, logo attached, exciting photos.
Should not have
• A lot of militia photos.

```html
<!DOCTYPE html>
<html lang="en">
<head>
<meta charset="utf-8">
<title>Trueshot Indoor Gun Range</title>
<link rel="stylesheet" href="https://fonts.googleapis.com/css2?family=Exo+2:wght@600;700&family=Arimo:ital,wght@0,400;0,700;1,400&display=swap">
<style>
:root{
  --page-top:#f0f0f0;
  --page-mid:#e2e2e2;
  --page-low:#6a6a6a;
  --nav-bg:#2e3032;
  --nav-border:#454749;
  --nav-text:#f2f2f2;
  --accent:#c4161c;
  --ink:#2b2b2b;
  --ink-soft:#444;
  --panel-dark:#2c2d2e;
  --card-top:#5a5b5c;
  --card-bottom:#3e3f40;
  --box-head-top:#4d5152;
  --box-head-bottom:#2f3233;
  --white:#ffffff;
  --divider:#d6d6d6;
  --footer-bg:#363839;
  --footer-line:#8a8c8e;
}
*{box-sizing:border-box;margin:0;padding:0}
html,body{width:1200px;height:1017px;overflow:hidden}
body{
  position:relative;
  font-family:"Arimo",Arial,sans-serif;
  background:linear-gradient(to bottom,var(--page-top) 0,var(--page-mid) 560px,#b9b9b9 760px,var(--page-low) 960px);
  color:var(--ink);
}
.top-strip{position:absolute;left:0;top:0;width:1200px;height:37px;background:#dcdcdc;border-bottom:2px solid #cfcfcf}
.main-nav{position:absolute;left:435px;top:0;height:35px;right:0;background:var(--nav-bg);display:flex}
.main-nav a{
  display:flex;align-items:center;justify-content:center;
  height:35px;color:var(--nav-text);text-decoration:none;
  font-family:"Exo 2",sans-serif;font-weight:600;font-size:14px;
  border-left:1px solid var(--nav-border);
}
.main-nav a.is-current{border-bottom:3px solid var(--accent);background:#3a3c3e}
.brand{position:absolute;left:82px;top:70px;display:flex;align-items:center;gap:14px}
.brand-name{
  font-family:"Exo 2",sans-serif;font-weight:700;font-size:22px;line-height:24px;
  color:var(--accent);text-transform:uppercase;letter-spacing:.5px;
}
.brand-dot{width:40px;height:40px;border-radius:50%;background:var(--accent)}
.hero{
  position:absolute;left:77px;top:143px;width:1047px;height:402px;
  background:var(--panel-dark);border-radius:4px;
  box-shadow:0 14px 18px rgba(0,0,0,.35);
}
.hero-photo{
  position:absolute;left:16px;top:15px;width:769px;height:369px;
  background:radial-gradient(ellipse at 55% 45%,#8a8a8a 0,#3b3b3b 35%,#0c0c0c 75%);
  border:1px solid #555;
}
.hero-card{
  position:absolute;left:796px;width:230px;border-radius:5px;
  background:linear-gradient(to bottom,var(--card-top),var(--card-bottom));
  padding:14px 16px;color:var(--white);
}
.hero-card h2{font-family:"Exo 2",sans-serif;font-weight:700;font-size:19px;margin-bottom:10px;text-shadow:0 1px 2px rgba(0,0,0,.6)}
.hero-card p{font-size:13px;line-height:19px;color:#eee}
.hero-card svg{position:absolute;right:14px;bottom:12px}
.card-range{top:22px;height:114px}
.card-specials{top:143px;height:112px}
.card-join{top:264px;height:116px}
.info-box{
  position:absolute;top:592px;width:334px;height:305px;background:var(--white);
  border-radius:6px;box-shadow:0 2px 6px rgba(0,0,0,.3);padding:7px 7px 0;
}
.box-events{left:76px}
.box-specials{left:432px}
.box-reviews{left:789px}
.box-head{
  height:48px;border-radius:3px;display:flex;align-items:center;justify-content:space-between;
  padding:0 26px 0 24px;color:var(--white);
  background:linear-gradient(to bottom,var(--box-head-top),var(--box-head-bottom));
}
.box-head h3{font-family:"Exo 2",sans-serif;font-weight:700;font-size:20px}
.box-head span{font-size:14px;color:#ddd}
.event{position:relative;margin:0 25px 0 17px;padding:18px 0 12px;border-bottom:1px solid var(--divider);height:78px}
.event:last-child{border-bottom:0}
.event h4{color:#a4161a;font-size:14px;font-weight:700;line-height:17px}
.event p{font-size:13px;line-height:19px;color:var(--ink-soft)}
.event em{font-size:13px;color:var(--ink-soft)}
.event svg{position:absolute;right:0;top:23px}
.list-item{display:flex;gap:15px;margin:13px 0 0 18px;height:63px}
.list-item:first-of-type{margin-top:19px}
.thumb{width:62px;height:62px;border:1px solid #ccc;padding:3px;background:var(--white);flex:none}
.thumb div{width:100%;height:100%;background:linear-gradient(135deg,#d8d8d8,#7a7a7a)}
.list-item h4{font-size:14px;font-weight:700;color:var(--ink);line-height:17px;margin-top:1px}
.list-item p{font-size:13px;line-height:19px;color:var(--ink-soft)}
.price{color:#b3141a;font-size:13px;font-weight:700}
.read{color:#b3141a;font-size:13px}
.site-footer{
  position:absolute;left:0;top:963px;width:1200px;height:54px;background:var(--footer-bg);
  border-top:6px solid var(--footer-line);
}
.site-footer p{position:absolute;right:81px;top:16px;color:#e6e6e6;font-size:14px}
</style>
</head>
<body>
<div class="top-strip"></div>
<nav class="main-nav">
  <a href="#" class="is-current" style="width:73px">Home</a>
  <a href="#" style="width:105px">The Range</a>
  <a href="#" style="width:120px">Range News</a>
  <a href="#" style="width:89px">Specials</a>
  <a href="#" style="width:118px">Membership</a>
  <a href="#" style="width:89px">Reviews</a>
  <a href="#" style="width:73px">About</a>
  <a href="#" style="width:98px">Contact</a>
</nav>

<header class="brand">
  <div class="brand-name">Trueshot<br>Indoor Gun Range</div>
  <div class="brand-dot"></div>
</header>

<section class="hero">
  <div class="hero-photo" role="img" aria-label="Close-up photograph of a polished steel revolver on a dark background"></div>
  <div class="hero-card card-range">
    <h2>Shooting Range</h2>
    <p>Training<br>Indoor &amp; outdoor<br>Target practice</p>
    <svg width="46" height="46" viewBox="0 0 46 46" fill="none" stroke="#1f1f1f" stroke-width="3"><circle cx="23" cy="23" r="19"/><circle cx="23" cy="23" r="10"/><circle cx="23" cy="23" r="3" fill="#1f1f1f"/><path d="M23 0v12M23 34v12M0 23h12M34 23h12"/></svg>
  </div>
  <div class="hero-card card-specials">
    <h2>Specials / Packages</h2>
    <p>Open Day Training<br>Clay shooting<br>and more!</p>
    <svg width="64" height="40" viewBox="0 0 64 40"><path d="M4 6h58v10H30l-4 6h-6l-6 16H2l6-18-4-2z" fill="#1f1f1f"/></svg>
  </div>
  <div class="hero-card card-join">
    <h2>Join Today!</h2>
    <p>Become a member<br>Up your skill level<br>Receive benefits</p>
    <svg width="40" height="76" viewBox="0 0 40 76"><circle cx="20" cy="14" r="11" fill="#1f1f1f"/><path d="M2 76V40q0-12 18-14 18 2 18 14v36z" fill="#1f1f1f"/></svg>
  </div>
</section>

<section class="info-box box-events">
  <div class="box-head"><h3>Upcoming Events</h3><span>...more</span></div>
  <div class="event">
    <h4>Clay Pigeon Shooting</h4><p>Shoot moving targets</p><em>Medium level</em>
    <svg width="38" height="38" viewBox="0 0 38 38"><circle cx="19" cy="19" r="17" fill="#f1f1f1" stroke="#bbb"/><path d="M16 12l7 7-7 7" fill="none" stroke="#333" stroke-width="3"/></svg>
  </div>
  <div class="event">
    <h4>Ladies Day Out</h4><p>Target Practice for the Ladies</p><em>Entry to Medium level</em>
    <svg width="38" height="38" viewBox="0 0 38 38"><circle cx="19" cy="19" r="17" fill="#f1f1f1" stroke="#bbb"/><path d="M16 12l7 7-7 7" fill="none" stroke="#333" stroke-width="3"/></svg>
  </div>
  <div class="event">
    <h4>Pistol Practice</h4><p>Handgun target challenge</p><em>Entry to Medium level</em>
    <svg width="38" height="38" viewBox="0 0 38 38"><circle cx="19" cy="19" r="17" fill="#f1f1f1" stroke="#bbb"/><path d="M16 12l7 7-7 7" fill="none" stroke="#333" stroke-width="3"/></svg>
  </div>
</section>

<section class="info-box box-specials">
  <div class="box-head"><h3>Specials</h3><span>...more</span></div>
  <div class="list-item">
    <div class="thumb"><div role="img" aria-label="Compact pistol product photo"></div></div>
    <div><h4>Ridgeline C30</h4><p>Slim frame 9</p><span class="price">$ 790.00</span></div>
  </div>
  <div class="list-item">
    <div class="thumb"><div role="img" aria-label="Red dot sight product photo"></div></div>
    <div><h4>Keenpoint Mini K1</h4><p>Target red point</p><span class="price">$ 625.00</span></div>
  </div>
  <div class="list-item">
    <div class="thumb"><div role="img" aria-label="Full-size pistol product photo"></div></div>
    <div><h4>Ridgeline F26 Pistol, Rx40</h4><p>Rx40 durable features</p><span class="price">$ 875.00</span></div>
  </div>
</section>

<section class="info-box box-reviews">
  <div class="box-head"><h3>Latest Reviews</h3><span>...more</span></div>
  <div class="list-item">
    <div class="thumb"><div role="img" aria-label="Revolver cylinder photo"></div></div>
    <div><h4>Revolver over the Years</h4><p>Revolver handguns</p><span class="read">...read article</span></div>
  </div>
  <div class="list-item">
    <div class="thumb"><div role="img" aria-label="Black 9mm pistol photo"></div></div>
    <div><h4>Vantage Pro, 9mm Model</h4><p>Vantage pistol series</p><span class="read">...read article</span></div>
  </div>
  <div class="list-item">
    <div class="thumb"><div role="img" aria-label="Holster with pistol photo"></div></div>
    <div><h4>Ironhawk Holsta</h4><p>Issued to military &amp; police units</p><span class="read">...read article</span></div>
  </div>
</section>

<footer class="site-footer"><p>© 2012&nbsp; Trueshot Indoor Gun Range</p></footer>
</body>
</html>
```